Small business that sells dolls used in the investigation of sudden infant deaths needs a website de

We need a modern update to our very simple current website. We are a small business that manufactures and sells featureless dolls used in the training and investigation of sudden infant deaths. With our customer base being primarily government organizations we are looking for design that is to the point and functional while also being engaging.

Target Market(s)

Our target audience are organizations such as government offices and training organizations looking for information about our product. This makes readability and ease-of-use of the design very important.

Number of Pages Required

5+ page

Font styles to use
Serif

Colors

Designer to choose colors to be used in the design.

Requirements
Must have
• Straightforward website focused towards the product being sold. With secondary focus is being how to contact the business and the care and use of the product. The business logo is orange and blue, these colors do not necessarily need to show up in the website design. Darker and muted/contrasting colors would probably be better.
Nice to have
• It would be nice if the website had a professional feel, that is slightly maternal but is not cutesy. Given the nature of our product, we also would like a site that is very respectful for any case that our product might be used in it.

```html
<!DOCTYPE html>
<html lang="en">
<head>
<meta charset="utf-8">
<title>Gentle Haven SUIDI Dolls</title>
<link href="https://fonts.googleapis.com/css2?family=Roboto:ital,wght@0,400;0,500;0,700;0,900;1,400&display=swap" rel="stylesheet">
<style>
:root{
  --orange:#e8512a;
  --blue:#2f86d6;
  --blue-dark:#1f6fbf;
  --ink:#1d1d1f;
  --text:#6b6f76;
  --line:#d8dde4;
  --mist:#eef2f7;
  --footer:#1b1b1d;
  --white:#ffffff;
}
*{margin:0;padding:0;box-sizing:border-box}
html,body{width:1200px;height:3488px;overflow:hidden}
body{font-family:"Roboto",Arial,sans-serif;color:var(--ink);background:var(--white);position:relative}
.abs{position:absolute}
.btn{position:absolute;display:flex;align-items:center;justify-content:center;border-radius:26px;font-weight:700;font-size:15px;letter-spacing:.5px;text-transform:uppercase}
.btn-solid{background:var(--orange);color:var(--white)}
.btn-outline{border:2px solid var(--orange);color:var(--orange)}
.btn-light{border:2px solid var(--white);color:var(--white)}

/* header */
.site-header{position:absolute;left:0;top:0;width:1200px;height:80px;background:var(--white);box-shadow:0 2px 6px rgba(0,0,0,.06);z-index:3}
.brand{position:absolute;left:28px;top:14px;display:flex;align-items:center;gap:12px}
.brand-dot{width:50px;height:50px;border-radius:50%;background:var(--blue)}
.brand-name{font-weight:700;font-size:20px;color:var(--ink)}
.topbar{position:absolute;right:30px;top:12px;display:flex;gap:28px;font-size:14px;color:var(--ink)}
.topbar span{display:flex;align-items:center;gap:8px}
.main-nav{position:absolute;right:30px;top:48px;display:flex;gap:34px;font-size:15px;font-weight:500}
.main-nav a{color:var(--ink);text-decoration:none}
.main-nav a.active{color:var(--orange);border-bottom:2px solid var(--orange);padding-bottom:4px}

/* hero */
.hero{position:absolute;left:0;top:80px;width:1200px;height:640px;overflow:hidden}
.hero-photo{position:absolute;inset:0;
  background:
    radial-gradient(ellipse 380px 200px at 78% 72%,rgba(240,120,110,.9),rgba(240,120,110,0) 70%),
    radial-gradient(ellipse 300px 160px at 95% 88%,rgba(226,96,88,.95),rgba(226,96,88,0) 70%),
    radial-gradient(ellipse 260px 140px at 62% 92%,rgba(232,110,100,.9),rgba(232,110,100,0) 70%),
    linear-gradient(180deg,#25292d 0%,#3b3f43 30%,#5c5552 48%,#b5615b 64%,#d8716a 80%,#c9625c 100%)}
.hero-title{position:absolute;left:108px;top:200px;width:480px;font-size:44px;font-weight:700;line-height:1.18;color:var(--ink)}

/* welcome */
.welcome-title{left:108px;top:810px;font-size:32px;font-weight:700;line-height:1.25;text-transform:uppercase}
.welcome-text{left:108px;top:905px;width:420px;font-size:16px;line-height:1.6;color:var(--text)}
.features{left:610px;top:820px;width:480px;list-style:none}
.features li{display:flex;gap:16px;font-size:16px;line-height:1.6;color:var(--text);margin-bottom:34px}
.tick{flex:0 0 24px;height:24px;border-radius:50%;background:var(--blue);margin-top:2px;display:flex;align-items:center;justify-content:center}

/* product */
.product{position:absolute;left:0;top:1220px;width:1200px;height:480px;background:var(--blue)}
.product-shot{position:absolute;top:90px;height:320px;box-shadow:0 10px 26px rgba(0,0,0,.25)}
.shot-red{left:108px;width:240px;
  background:
    radial-gradient(ellipse 90px 140px at 50% 52%,#e2452c 0%,#e65a3e 45%,rgba(236,120,96,.45) 75%,rgba(247,247,247,0) 100%),
    linear-gradient(180deg,#fbfbfb,#ececec)}
.shot-white{left:380px;width:270px;
  background:
    radial-gradient(ellipse 80px 135px at 50% 52%,#f4f4f4 0%,#d9d9d9 50%,rgba(120,120,120,.35) 80%,rgba(15,15,15,0) 100%),
    linear-gradient(180deg,#111,#050505)}
.product-title{left:740px;top:105px;font-size:34px;font-weight:700;color:var(--white);text-transform:uppercase}
.product-text{left:740px;top:165px;width:400px;font-size:15px;line-height:1.65;color:#e6f0fb}

/* sids */
.sids-title{left:0;width:1200px;top:1790px;text-align:center;font-size:32px;font-weight:700;text-transform:uppercase}
.sids-text{left:250px;width:700px;top:1860px;text-align:center;font-size:15px;line-height:1.65;color:var(--text)}
.cause{position:absolute;width:240px}
.cause h3{font-size:20px;font-weight:500;color:var(--ink)}
.cause p{font-size:14px;color:var(--text);margin-top:6px}
.cause.left{text-align:right}

/* testimonials */
.testimonials{position:absolute;left:0;top:2400px;width:1200px;height:600px;background:var(--mist)}
.t-title{left:0;width:1200px;top:80px;text-align:center;font-size:32px;font-weight:700;text-transform:uppercase}
.t-stars{left:0;width:1200px;top:135px;text-align:center;color:var(--orange);font-size:22px;letter-spacing:4px}
.t-quote{left:250px;width:700px;top:175px;text-align:center;font-style:italic;font-size:15px;line-height:1.7;color:var(--text)}
.avatar{position:absolute;border-radius:50%;background:#c9ced6}
.t-name{left:0;width:1200px;top:405px;text-align:center;font-size:17px;font-weight:700;text-transform:uppercase}
.t-role{left:0;width:1200px;top:430px;text-align:center;font-size:13px;color:var(--text)}

/* footer */
.site-footer{position:absolute;left:0;top:2960px;width:1200px;height:528px;background:var(--footer);color:#cfd2d6}
.f-brand{position:absolute;left:90px;top:80px;width:230px;text-align:center}
.f-brand .ring{width:170px;height:170px;border-radius:50%;background:var(--blue);margin:0 auto 18px}
.f-brand .name{font-size:20px;font-weight:700;color:var(--white)}
.f-col{position:absolute;top:155px}
.f-col h4{font-size:18px;font-weight:700;color:var(--white);margin-bottom:16px}
.f-col li{list-style:none;font-size:14px;line-height:1.95}
.f-col p{font-size:14px;line-height:1.6}
.f-input{width:240px;height:40px;background:var(--white);border-radius:4px;margin-top:16px;padding:0 14px;display:flex;align-items:center;color:#9aa0a6;font-size:13px}
.contact-row{display:flex;gap:10px;font-size:14px;line-height:1.5;margin-bottom:16px}
.f-bottom{position:absolute;left:0;top:440px;width:1200px;border-top:1px solid #34363a}
.copyright{position:absolute;left:40px;top:32px;font-size:13px}
.social{position:absolute;right:70px;top:24px;display:flex;gap:12px}
.social span{width:32px;height:32px;border-radius:50%;border:2px solid var(--orange)}
</style>
</head>
<body>

<header class="site-header">
  <div class="brand"><div class="brand-dot"></div><div class="brand-name">Gentle Haven SUIDI Dolls</div></div>
  <div class="topbar">
    <span><svg width="14" height="14" viewBox="0 0 24 24"><path fill="#e8512a" d="M6.6 10.8a15 15 0 0 0 6.6 6.6l2.2-2.2a1 1 0 0 1 1-.25 11.4 11.4 0 0 0 3.6.6 1 1 0 0 1 1 1V20a1 1 0 0 1-1 1A17 17 0 0 1 3 4a1 1 0 0 1 1-1h3.5a1 1 0 0 1 1 1c0 1.25.2 2.45.6 3.6a1 1 0 0 1-.25 1z"/></svg>(555) 014-2020</span>
    <span><svg width="16" height="14" viewBox="0 0 24 18"><rect x="1" y="1" width="22" height="16" rx="2" fill="none" stroke="#e8512a" stroke-width="2"/><path d="M1 2l11 8 11-8" fill="none" stroke="#e8512a" stroke-width="2"/></svg>hello@gentlehavendolls.com</span>
  </div>
  <nav class="main-nav">
    <a class="active" href="#">Home</a><a href="#">Order</a><a href="#">Contact</a><a href="#">Care &amp; Use of Dolls</a><a href="#">About Us</a>
    <svg width="16" height="16" viewBox="0 0 24 24" style="margin-top:2px"><circle cx="10" cy="10" r="7" fill="none" stroke="#1d1d1f" stroke-width="2.5"/><path d="M15 15l7 7" stroke="#1d1d1f" stroke-width="2.5"/></svg>
  </nav>
</header>

<section class="hero">
  <div class="hero-photo" role="img" aria-label="Photo of many red weighted investigation dolls laid out on a conference table"></div>
  <svg class="abs" style="left:0;top:0" width="1200" height="640" viewBox="0 0 1200 640">
    <path d="M0 0 H520 C780 140 790 470 620 640 H0 Z" fill="#ffffff"/>
    <path d="M520 0 C780 140 790 470 620 640" fill="none" stroke="#2f86d6" stroke-width="6"/>
  </svg>
  <h1 class="hero-title">Investigation dolls for sudden, unexplained infant death</h1>
  <div class="btn btn-solid" style="left:108px;top:410px;width:200px;height:52px">Order Online</div>
</section>

<h2 class="abs welcome-title">Welcome to<br>Gentle Haven SUIDI Dolls</h2>
<p class="abs welcome-text">Our online store offers weighted dolls that are used by investigators to reenact and photograph scenes of sudden, unexplained infant death.</p>
<div class="btn btn-outline" style="left:108px;top:1058px;width:140px;height:44px">Read More</div>
<ul class="abs features">
  <li><span class="tick"><svg width="12" height="12" viewBox="0 0 12 12"><path d="M2 6l3 3 5-6" fill="none" stroke="#fff" stroke-width="2"/></svg></span>The tan or light-pound featureless dolls are made of light coloured fabric or orange high-visibility fabric for photographic purposes.</li>
  <li><span class="tick"><svg width="12" height="12" viewBox="0 0 12 12"><path d="M2 6l3 3 5-6" fill="none" stroke="#fff" stroke-width="2"/></svg></span>The orange fabric may be wiped with a germicidal solution using a damp rag.</li>
  <li><span class="tick"><svg width="12" height="12" viewBox="0 0 12 12"><path d="M2 6l3 3 5-6" fill="none" stroke="#fff" stroke-width="2"/></svg></span>A permanent marker may be used to mark the front and back or add facial features as desired.</li>
</ul>

<section class="product">
  <div class="product-shot shot-red" role="img" aria-label="Photo of an orange featureless investigation doll on a white background"></div>
  <div class="product-shot shot-white" role="img" aria-label="Photo of a white featureless investigation doll on a black background"></div>
  <h2 class="abs product-title">Our Product</h2>
  <p class="abs product-text">Gentle Haven accepts credit cards, purchase orders and personal checks. For credit card purchases we will contact you to obtain the required information. All forms provided upon request. We are on contract for Washington State purchases.</p>
  <div class="btn btn-light" style="left:740px;top:340px;width:150px;height:44px">Order Now</div>
</section>

<h2 class="abs sids-title">Sudden Infant Death Syndrome</h2>
<p class="abs sids-text">The Evergreen Infant Loss Foundation contacted us about making dolls for investigators. With their help we have designed a doll that we have made available to the sudden, unexplained infant death (SUIDI) investigation community.</p>

<svg class="abs" style="left:0;top:1960px" width="1200" height="360" viewBox="0 0 1200 360">
  <circle cx="600" cy="165" r="190" fill="#f4f6f9"/>
  <g stroke="#c9d3df" stroke-width="2">
    <line x1="600" y1="165" x2="395" y2="70"/><line x1="600" y1="165" x2="805" y2="70"/>
    <line x1="600" y1="165" x2="395" y2="260"/><line x1="600" y1="165" x2="805" y2="260"/>
  </g>
  <circle cx="600" cy="165" r="72" fill="#fff" stroke="#2f86d6" stroke-width="6"/>
  <circle cx="600" cy="165" r="30" fill="#e8512a"/>
  <g fill="#fff" stroke="#e4e8ee" stroke-width="2">
    <circle cx="395" cy="70" r="30"/><circle cx="805" cy="70" r="30"/>
    <circle cx="395" cy="260" r="30"/><circle cx="805" cy="260" r="30"/>
  </g>
  <path d="M395 84 l-12-12 a7 7 0 0 1 12-9 a7 7 0 0 1 12 9z" fill="#e8512a"/>
  <g fill="#e8512a"><circle cx="805" cy="70" r="9"/><circle cx="793" cy="60" r="3"/><circle cx="818" cy="60" r="3"/><circle cx="793" cy="82" r="3"/><circle cx="818" cy="82" r="3"/></g>
  <path d="M389 246 h12 v6 l4 6 v16 h-20 v-16 l4-6z" fill="#e8512a"/>
  <g fill="#e8512a"><circle cx="805" cy="260" r="7"/><circle cx="795" cy="250" r="4"/><circle cx="816" cy="252" r="4"/><circle cx="798" cy="272" r="4"/><circle cx="815" cy="270" r="3"/></g>
</svg>
<div class="cause left" style="left:110px;top:2008px"><h3>SIDS</h3><p>Sudden death in sleep</p></div>
<div class="cause" style="left:850px;top:2008px"><h3>Infections</h3><p>Rapid illness onset</p></div>
<div class="cause left" style="left:110px;top:2198px"><h3>Poisoning or overdose</h3><p>Accidental exposure</p></div>
<div class="cause" style="left:850px;top:2198px"><h3>Inborn errors</h3><p>Metabolic conditions</p></div>
<div class="btn btn-outline" style="left:530px;top:2310px;width:140px;height:44px">Read More</div>

<section class="testimonials">
  <h2 class="abs t-title">Client Testimonials</h2>
  <div class="abs t-stars">★★★★☆</div>
  <p class="abs t-quote">These dolls gave our investigators a respectful and practical way to document each scene. The quality is consistent, orders arrive quickly and the team is always helpful.</p>
  <div class="avatar" role="img" aria-label="Client portrait" style="left:488px;top:292px;width:64px;height:64px"></div>
  <div class="avatar" role="img" aria-label="Client portrait" style="left:556px;top:280px;width:88px;height:88px;background:#9aa2ad;border:3px solid #fff"></div>
  <div class="avatar" role="img" aria-label="Client portrait" style="left:648px;top:292px;width:64px;height:64px"></div>
  <div class="abs t-name">Daniel Moore</div>
  <div class="abs t-role">County Death Investigator</div>
  <svg class="abs" style="left:0;top:500px" width="1200" height="100" viewBox="0 0 1200 100">
    <path d="M0 40 Q600 -20 1200 40 V100 H0Z" fill="#2f86d6"/>
    <path d="M0 70 Q600 10 1200 70 V100 H0Z" fill="#1b1b1d"/>
  </svg>
</section>

<footer class="site-footer">
  <div class="f-brand"><div class="ring"></div><div class="name">Gentle Haven SUIDI Dolls</div></div>
  <div class="f-col" style="left:400px"><h4>Information</h4><ul><li>Help</li><li>FAQ</li><li>Support</li><li>Sitemap</li><li>Terms Of Use</li><li>Privacy Statement</li></ul></div>
  <div class="f-col" style="left:590px;width:260px"><h4>Newsletter Subscription</h4><p>Register your email address to get information about us</p>
    <div class="f-input">Email Address</div>
    <div class="btn btn-solid" style="position:relative;margin-top:16px;width:150px;height:44px">Subscribe</div></div>
  <div class="f-col" style="left:890px;width:240px"><h4>Contact Us</h4>
    <div class="contact-row"><svg width="14" height="18" viewBox="0 0 14 20"><path d="M7 0a7 7 0 0 1 7 7c0 5-7 13-7 13S0 12 0 7a7 7 0 0 1 7-7z" fill="#e8512a"/><circle cx="7" cy="7" r="2.5" fill="#1b1b1d"/></svg><span>420 Alder Lane<br>Maple Grove, WA 98000</span></div>
    <div class="contact-row"><svg width="14" height="14" viewBox="0 0 24 24"><path fill="#e8512a" d="M6.6 10.8a15 15 0 0 0 6.6 6.6l2.2-2.2a1 1 0 0 1 1-.25 11.4 11.4 0 0 0 3.6.6 1 1 0 0 1 1 1V20a1 1 0 0 1-1 1A17 17 0 0 1 3 4a1 1 0 0 1 1-1h3.5a1 1 0 0 1 1 1c0 1.25.2 2.45.6 3.6a1 1 0 0 1-.25 1z"/></svg><span>(555) 014-2020</span></div>
    <div class="contact-row"><svg width="16" height="14" viewBox="0 0 24 18"><rect x="1" y="1" width="22" height="16" rx="2" fill="none" stroke="#e8512a" stroke-width="2"/><path d="M1 2l11 8 11-8" fill="none" stroke="#e8512a" stroke-width="2"/></svg><span>hello@gentlehavendolls.com</span></div>
  </div>
  <div class="f-bottom">
    <div class="copyright">Copyright © 2019, Gentle Haven SUIDI Dolls. All rights reserved.</div>
    <div class="social"><span></span><span></span><span></span></div>
  </div>
</footer>

</body>
</html>
```